Summit Vigor & Coaching needs a Flyer design

Need a flyer for a letterbox drop advertising mobile personal training services and new home studio in the local area. Offer personalised fitness training in the privacy of your own home, or with fitness equipment at our local home studio. Private sessions and Group Classes available, visit www.zelwintrahealth.com.au for more detailed information on our services. I have uploaded our logo that has been designed. Our target market is middle aged women & men.
Updates
Target Market(s)
Middle aged women & men
Industry/Entity Type
Advertising
Look and feel
Each slider illustrates characteristics of the customer's brand and the style your logo design should communicate.

```html
<!DOCTYPE html>
<html lang="en">
<head>
<meta charset="utf-8">
<title>Summit Vigor &amp; Coaching – Flyer</title>
<link rel="stylesheet" href="https://fonts.googleapis.com/css2?family=Oswald:wght@500;600;700&family=Zilla+Slab:wght@700&family=Anton&display=swap">
<style>
  :root {
    --ink-black: #0d0f12;
    --paper-white: #ffffff;
    --sky-cyan: #5fd3ea;
    --band-cyan: #58c9e4;
    --band-blue: #2f8fcf;
    --box-blue: #3a8bc9;
    --deep-blue: #1f6fae;
    --brand-blue: #4aa6dc;
    --text-dark: #1d2a36;
  }
  * { box-sizing: border-box; margin: 0; padding: 0; }
  html, body {
    width: 993px; height: 1200px; overflow: hidden;
    background: var(--ink-black);
  }
  .flyer {
    position: relative; width: 993px; height: 1200px; overflow: hidden;
    background: var(--ink-black);
    font-family: "Oswald", "Arial Narrow", sans-serif;
  }

  /* Photo area */
  .hero-photo {
    position: absolute; left: 0; top: 0; width: 993px; height: 720px;
    background:
      radial-gradient(ellipse at 35% 60%, #d9a07c 0%, #b97a58 28%, transparent 55%),
      radial-gradient(ellipse at 80% 30%, #6f8f98 0%, transparent 60%),
      linear-gradient(160deg, #49656f 0%, #2c3f47 55%, #1a2429 100%);
  }

  /* White header with curved edge */
  .header-curve { position: absolute; left: 0; top: 0; width: 993px; height: 420px; }
  .brand {
    position: absolute; left: 0; top: 160px; width: 993px;
    text-align: center;
  }
  .brand-name {
    font-family: "Oswald", "Arial Narrow", sans-serif;
    font-weight: 500; font-size: 44px; letter-spacing: 2px;
    color: var(--brand-blue);
  }

  /* Service bands */
  .band-mobile {
    position: absolute; left: 0; top: 720px; width: 993px; height: 170px;
    background: var(--band-cyan);
  }
  .band-studio {
    position: absolute; left: 0; top: 890px; width: 993px; height: 150px;
    background: var(--band-blue);
  }

  .headline-box {
    position: absolute; border-radius: 10px;
    font-family: "Zilla Slab", Georgia, serif; font-weight: 700;
    color: var(--paper-white); text-transform: uppercase;
    line-height: 1; letter-spacing: 0.5px;
    text-shadow: 2px 3px 3px rgba(0,0,0,0.45);
  }
  .headline-mobile {
    left: 40px; top: 740px; width: 610px; height: 108px;
    background: var(--box-blue); padding: 8px 20px;
    font-size: 46px;
  }
  .headline-studio {
    left: 400px; top: 905px; width: 560px; height: 100px;
    background: var(--deep-blue); padding: 6px 20px;
    font-size: 44px; text-align: right;
  }
  .subline {
    position: absolute; font-weight: 600; font-size: 21px; letter-spacing: 0.4px;
    white-space: nowrap;
  }
  .subline-mobile { left: 48px; top: 854px; color: var(--text-dark); }
  .subline-studio { right: 36px; top: 1008px; color: var(--sky-cyan); }

  /* Badge */
  .badge { position: absolute; left: 60px; top: 900px; width: 290px; height: 290px; }
  .badge-text {
    position: absolute; left: 60px; top: 900px; width: 290px; height: 290px;
    display: flex; flex-direction: column; align-items: center; justify-content: center;
    color: var(--ink-black); text-transform: uppercase; text-align: center;
    transform: rotate(-8deg);
  }
  .badge-small { font-family: "Anton", "Impact", sans-serif; font-size: 21px; line-height: 1.1; }
  .badge-large { font-family: "Anton", "Impact", sans-serif; font-size: 40px; line-height: 1.15; }

  /* Contact */
  .contact {
    position: absolute; right: 36px; top: 1095px; text-align: right;
  }
  .contact-lead {
    font-weight: 700; font-size: 22px; color: var(--sky-cyan);
    letter-spacing: 0.6px; text-transform: uppercase;
  }
  .contact-web { font-weight: 600; font-size: 26px; color: var(--paper-white); margin-top: 6px; }
</style>
</head>
<body>
<main class="flyer">
  <div class="hero-photo" role="img" aria-label="Photo of a woman in a gym lifting dumbbells from a rack"></div>

  <svg class="header-curve" viewBox="0 0 993 420" aria-hidden="true">
    <path d="M0 0 H993 V250 Q560 430 0 410 Z" fill="#ffffff"/>
    <path d="M0 410 Q560 430 993 250" fill="none" stroke="#4aa6dc" stroke-width="5"/>
  </svg>

  <header class="brand">
    <p class="brand-name">Summit Vigor &amp; Coaching</p>
  </header>

  <section class="band-mobile"></section>
  <div class="headline-box headline-mobile">Mobile Personal<br>Training Services</div>
  <p class="subline subline-mobile">Personalised Fitness Training In The Privacy Of Your Own Home</p>

  <section class="band-studio"></section>
  <div class="headline-box headline-studio">New Home Studio<br>In The Local Area</div>
  <p class="subline subline-studio">With Fitness Equipment At Our Local Home Studio</p>

  <svg class="badge" viewBox="0 0 290 290" aria-hidden="true">
    <circle cx="145" cy="145" r="143" fill="#0d0f12"/>
    <circle cx="145" cy="145" r="128" fill="#9aa2aa"/>
    <circle cx="145" cy="145" r="118" fill="#d9dde1"/>
    <circle cx="145" cy="145" r="104" fill="#ffffff" stroke="#b8bec4" stroke-width="3"/>
  </svg>
  <div class="badge-text">
    <span class="badge-small">Private Sessions</span>
    <span class="badge-small">&amp; Group Classes</span>
    <span class="badge-large">Available</span>
  </div>

  <footer class="contact">
    <p class="contact-lead">For More Detailed Information On Our Services</p>
    <p class="contact-web">www.zelwintrahealth.com.au</p>
  </footer>
</main>
</body>
</html>
```